Carver Lindqvist Group Business Cards

We have a new logo, and want to design new business cards with it. We are 21 years in business, and want a fresh but professional look, so not a lot of extra stuff on the card. We are a recruiting and staffing firm focused on placing accounting and finance professionals in the Dallas TX area. I've attached our new logo that should be displayed on the cards. Here is what I think we want on the cards:
Ray Pemberly, CPA
Partner and Managing Director
8282 Orchard Vale Rd.
Suite 610
Dallas, TX 75391
O 214-555-0184
M 214-555-0237
ray@carverlindqvist.example
www.carverlindqvist.example

```html
<!DOCTYPE html>
<html lang="en">
<head>
<meta charset="utf-8">
<title>Carver Lindqvist Group — Business Cards</title>
<link rel="stylesheet" href="https://fonts.googleapis.com/css2?family=Montserrat:wght@600;700&family=Open+Sans:wght@400;600&display=swap">
<style>
  :root {
    --bg: #e9eef5;
    --paper: #ffffff;
    --navy: #1537a0;
    --panel: #4a66b3;
    --tint: #dfe4ef;
    --white: #ffffff;
  }
  * { margin: 0; padding: 0; box-sizing: border-box; }
  html, body { width: 1200px; height: 835px; overflow: hidden; background: var(--bg); }
  .canvas {
    width: 1200px; height: 835px;
    display: flex; align-items: center; justify-content: center; gap: 60px;
  }
  .card {
    position: relative; width: 525px; height: 300px;
    background: var(--paper); overflow: hidden;
    box-shadow: 0 6px 18px rgba(20, 40, 90, 0.15);
    font-family: "Open Sans", sans-serif;
  }
  .tint-shape {
    position: absolute; background: var(--tint);
    transform: rotate(-30deg);
  }
  .wordmark {
    position: absolute; display: flex; align-items: center; gap: 8px;
    font-family: "Montserrat", sans-serif; font-weight: 700;
    color: var(--navy); font-size: 17px; letter-spacing: 0.5px; text-transform: uppercase;
  }
  .wordmark .mark { width: 12px; height: 12px; background: var(--navy); flex: none; }

  /* front */
  .front .band {
    position: absolute; left: 0; right: 0; bottom: 0; height: 112px;
    background: var(--panel); border-top: 4px solid var(--navy);
  }
  .front .wordmark { left: 150px; top: 110px; }
  .name-pill {
    position: absolute; left: 130px; top: 170px; width: 270px; height: 56px;
    background: var(--navy); border-radius: 28px;
    outline: 3px solid var(--white); outline-offset: -7px;
    color: var(--white); text-align: center; padding-top: 10px;
  }
  .name-pill .name { font-family: "Montserrat", sans-serif; font-weight: 700; font-size: 16px; }
  .name-pill .title { font-size: 8px; }

  /* back */
  .back .panel {
    position: absolute; top: 0; bottom: 0; right: 0; width: 248px;
    background: var(--panel); border-left: 5px solid var(--navy);
  }
  .back .identity { position: absolute; left: 28px; top: 34px; color: var(--navy); }
  .back .identity .name { font-family: "Montserrat", sans-serif; font-weight: 700; font-size: 21px; white-space: nowrap; }
  .back .identity .title { font-size: 11px; }
  .back .wordmark { left: 28px; top: 138px; font-size: 14px; line-height: 1.25; }
  .back .wordmark .wordmark-text { display: block; width: 180px; }
  .icon-rail {
    position: absolute; left: 254px; top: 70px; width: 40px; height: 170px;
    background: var(--navy); border-radius: 20px;
    outline: 2px solid var(--white); outline-offset: -6px;
    display: flex; flex-direction: column; justify-content: space-around; align-items: center;
    padding: 14px 0;
  }
  .icon-rail svg { width: 18px; height: 18px; fill: none; stroke: var(--white); stroke-width: 1.6; stroke-linecap: round; stroke-linejoin: round; }
  .contact {
    position: absolute; left: 310px; top: 78px; color: var(--white);
    font-size: 11.5px; line-height: 1.45;
  }
  .contact p + p { margin-top: 12px; }
</style>
</head>
<body>
<main class="canvas">
  <section class="card front" aria-label="Card front">
    <div class="tint-shape" style="left:40px;top:-40px;width:70px;height:260px;"></div>
    <div class="tint-shape" style="left:140px;top:-60px;width:60px;height:240px;"></div>
    <div class="band"></div>
    <div class="wordmark"><span class="mark"></span>Carver Lindqvist Group</div>
    <div class="name-pill">
      <div class="name">RAY PEMBERLY, CPA</div>
      <div class="title">Partner and Managing Director</div>
    </div>
  </section>

  <section class="card back" aria-label="Card back">
    <div class="tint-shape" style="left:10px;top:170px;width:60px;height:200px;"></div>
    <div class="tint-shape" style="left:110px;top:190px;width:55px;height:180px;"></div>
    <div class="identity">
      <div class="name">RAY PEMBERLY, CPA</div>
      <div class="title">Partner and Managing Director</div>
    </div>
    <div class="wordmark"><span class="mark"></span><span class="wordmark-text">Carver Lindqvist Group</span></div>
    <div class="panel"></div>
    <div class="icon-rail">
      <svg viewBox="0 0 20 20" aria-label="Address"><path d="M3 10 10 3l7 7M5 8.5V17h10V8.5M8.5 17v-5h3v5"/></svg>
      <svg viewBox="0 0 20 20" aria-label="Email"><rect x="3" y="5" width="14" height="10"/><path d="M3 5l7 6 7-6"/></svg>
      <svg viewBox="0 0 20 20" aria-label="Phone"><path d="M5 3h3l1.5 4-2 1.5a9 9 0 0 0 4 4l1.5-2 4 1.5v3a2 2 0 0 1-2 2A14 14 0 0 1 3 5a2 2 0 0 1 2-2z"/></svg>
      <svg viewBox="0 0 20 20" aria-label="Website"><circle cx="10" cy="10" r="7"/><path d="M3 10h14M10 3c-3 4-3 10 0 14M10 3c3 4 3 10 0 14"/></svg>
    </div>
    <div class="contact">
      <p>8282 Orchard Vale Rd. Suite 610<br>Dallas, TX 75391</p>
      <p>ray@carverlindqvist.example</p>
      <p>O 214-555-0184<br>M 214-555-0237</p>
      <p>www.carverlindqvist.example</p>
    </div>
  </section>
</main>
</body>
</html>
```